Redesign of 3-4 page site for professional services firm

Our site is www.kestrelvaleadvisors.com. We currently have a simple page made with HostPlumo tools. But the tools are not able to generate the look and feel we desire. We need a home page similar to current that tells a little about our company, our experience and our team. We need a second page to show details of current and past transactions we have assisted our clients with. Currently this page reads like a word document but we would like for it to present in a cleaner fashion and liven it up with some images that link to the industry served. For example, a motorcycle outline in a circle for the powersports related transactions. We would like page to introduce each member of "Our Team" and highlight their experience with a photo of each person. If there is no photo available, we would like a placeholder to be their initials in a circle that can be updated later. We would also like a contact us section whether this is a different page or part of the home page.

Target Market(s)

Retirement minded business owners

Industry/Entity Type

Professional Services

Coding

Coded - Design and coding required

Requirements
Must have
• See project description. Must include a page or section for "Current Listings" and "Recently Completed Transactions" (can be same page)

```html
<!DOCTYPE html>
<html lang="en">
<head>
<meta charset="utf-8">
<title>Kestrel Vale Advisors</title>
<link href="https://fonts.googleapis.com/css2?family=Roboto+Condensed:wght@700&family=Catamaran:wght@600;700&family=Montserrat:wght@400;500;600;700&family=Alegreya:wght@500;700&display=swap" rel="stylesheet">
<style>
:root{
  --green:#0f9d0f;
  --red:#e02020;
  --olive:#c9c900;
  --ink:#1b1b1b;
  --text:#333;
  --muted:#bdbdbd;
  --soft:#f5f5f5;
  --line:#e2e2e2;
  --black:#000;
}
*{box-sizing:border-box;margin:0;padding:0}
html,body{width:1200px;height:4594px;overflow:hidden}
body{font-family:"Montserrat",sans-serif;color:var(--text);background:#fff;font-size:12px;line-height:1.9}
section,header,footer{position:relative;width:1200px}
.abs{position:absolute}
.brand{font-family:"Catamaran",sans-serif;font-weight:700;color:var(--ink);display:flex;align-items:center;gap:12px;letter-spacing:.5px}
.brand .mark{width:22px;height:22px;background:var(--green)}
.sec-title{font-family:"Catamaran",sans-serif;font-weight:700;font-size:30px;color:var(--ink);text-align:center;letter-spacing:.5px;line-height:1.2}
.rule{display:flex;gap:5px;justify-content:center;margin-top:8px}
.rule i{display:block;width:20px;height:3px}
.rule i:nth-child(1){background:var(--red)}
.rule i:nth-child(2){background:var(--olive)}
.rule i:nth-child(3){background:var(--green)}
.btn{display:inline-flex;align-items:center;justify-content:center;font-weight:600;font-size:13px;color:#fff;background:var(--green);letter-spacing:.5px}
.btn.olive{background:var(--olive);color:#333}
.photo{background:linear-gradient(135deg,#d9dde2,#8c96a3)}

/* header + hero */
.site-header{height:556px}
.site-header .brand{left:139px;top:38px;font-size:34px}
.nav{left:542px;top:34px;display:flex;gap:40px;font-size:11.5px;font-weight:600;color:var(--ink)}
.call{left:905px;top:22px;display:flex;gap:12px;align-items:center}
.call .ico{width:34px;height:34px;border-radius:50%;background:#333;display:flex;align-items:center;justify-content:center}
.call p{font-size:12px;line-height:1.3;color:#333}
.call b{font-size:15px;font-weight:500}
.hero-title{left:143px;top:226px;font-family:"Roboto Condensed",sans-serif;font-size:47px;line-height:1.17;color:var(--ink)}
.hero-sub{left:145px;top:346px;font-size:13px;font-weight:600;color:var(--ink)}
.hero-btn{left:143px;top:392px;width:126px;height:41px}
.hero-photo{left:620px;top:70px;width:496px;height:486px;background:linear-gradient(160deg,#eef3ea 0%,#c7d6c0 55%,#7f9a6f 100%)}

/* about */
.about{height:560px;background:var(--soft)}
.about .frame{left:127px;top:70px;width:410px;height:300px;border:3px solid var(--red);border-right:none;border-bottom:none}
.about .photo{left:86px;top:80px;width:462px;height:420px}
.about h2{left:596px;top:126px;font-family:"Catamaran",sans-serif;font-size:32px;font-weight:700;color:var(--ink);letter-spacing:.5px;line-height:1.2}
.about .rule{left:596px;top:172px;position:absolute;margin:0}
.about .copy{left:596px;top:186px;width:466px;font-size:11.6px;line-height:2}
.about .btn{left:596px;top:394px;width:126px;height:40px}

/* experience */
.experience{height:583px}
.experience .head{top:80px;left:0;width:1200px}
.card{background:#fff;box-shadow:0 1px 8px rgba(0,0,0,.14);display:flex;align-items:center;gap:18px;padding:0 18px 0 14px;font-size:11.3px;line-height:1.8}
.card .ico{flex:none;width:60px;height:60px;border-radius:50%;background:#eef3ee;border:2px solid #d7e6d7}
.exp-logo{left:630px;top:470px;font-size:32px}
.experience .btn{left:888px;top:453px;width:127px;height:41px}

/* team */
.team{height:892px;background:var(--soft)}
.team .head{top:88px;left:0;width:1200px}
.team .intro{left:171px;top:150px;width:870px;text-align:center;font-size:11.6px;line-height:2}
.member{top:300px;width:240px;text-align:center}
.member .avatar{width:214px;height:214px;border-radius:50%;margin:0 auto;background:linear-gradient(180deg,#d4d4d4,#8a8a8a)}
.member h3{font-family:"Alegreya",serif;font-weight:500;font-size:18px;color:var(--ink);margin-top:22px;line-height:1.2}
.member p{font-size:11.5px;color:#444;line-height:1.6}
.bio{left:153px;top:619px;width:892px;height:188px;background:#fff;box-shadow:0 1px 10px rgba(0,0,0,.15);padding:24px 16px}
.bio h3{font-family:"Alegreya",serif;font-weight:500;font-size:30px;color:var(--ink);line-height:1.2;margin-bottom:10px}
.bio p{font-size:11.4px;line-height:2}

/* listing */
.listing{height:618px}
.listing .head{top:80px;left:0;width:1200px}
.tabs{left:300px;top:146px;display:flex;gap:48px;font-family:"Alegreya",serif;font-size:20px;font-weight:500}
.tabs .on{color:var(--ink);border-bottom:2px solid var(--ink);padding-bottom:2px}
.tabs .off{color:var(--muted)}
.deal{left:189px;top:280px;width:470px}
.deal h3{font-family:"Alegreya",serif;font-weight:500;font-size:22px;color:var(--ink);line-height:1.2}
.deal .amt{font-size:11.6px;font-weight:600;color:var(--ink);margin:6px 0 4px}
.deal p{font-size:11.5px;line-height:2}
.deal .btn{margin-top:16px;width:127px;height:41px}
.listing .frame{left:711px;top:226px;width:298px;height:246px;border:3px solid var(--red);border-left:none;border-bottom:none}
.listing .photo{left:703px;top:233px;width:295px;height:298px}

/* testimonials */
.reviews{height:505px;background:var(--soft)}
.reviews .head{top:82px;left:0;width:1200px}
.quote{top:186px;width:425px;height:235px;background:#fff;box-shadow:0 1px 8px rgba(0,0,0,.12);padding:28px 16px}
.quote .who{display:flex;align-items:center;gap:20px;font-size:14px;font-weight:500;color:var(--ink)}
.quote .face{width:52px;height:52px;border-radius:50%;background:linear-gradient(135deg,#cfd6de,#7d8794);border:3px solid #e9e9e9}
.quote .mark{position:absolute;right:16px;top:16px}
.quote h4{font-family:"Alegreya",serif;font-weight:700;font-size:15px;color:var(--ink);margin-top:18px}
.quote p{font-size:11.3px;line-height:2}
.arrow{top:290px;width:28px;height:28px;border:1.5px solid #333;border-radius:50%;display:flex;align-items:center;justify-content:center;background:#fff}

/* inquiry */
.inquiry{height:499px}
.inquiry .head{top:92px;left:0;width:1200px}
.field{height:40px;border:1px solid var(--line);display:flex;align-items:center;gap:8px;padding:0 10px;font-size:11.5px;color:#555;background:#fff}
.field.msg{align-items:flex-start;padding-top:10px;height:78px}
.inquiry .btn{left:537px;top:378px;width:128px;height:37px}

/* footer */
.site-footer{height:381px;background:var(--black);color:#fff}
.site-footer .brand{left:0;width:1200px;top:62px;justify-content:center;color:#fff;font-size:40px;line-height:1.2}
.f-col h4{font-family:"Catamaran",sans-serif;font-weight:600;font-size:17px;letter-spacing:.5px;line-height:1.2;margin-bottom:6px}
.f-links{left:143px;top:188px}
.f-links a{display:block;color:#fff;text-decoration:none;font-size:11.5px;line-height:1.95}
.f-news{left:357px;top:186px}
.f-news p{font-size:11.5px}
.f-news .form{display:flex;gap:12px;margin-top:10px}
.f-news .in{width:229px;height:41px;background:#fff;color:#333;font-size:11px;display:flex;align-items:center;padding:0 12px}
.f-news .go{width:112px;height:41px;background:var(--olive);color:#333;font-size:14px;display:flex;align-items:center;justify-content:center}
.f-contact{left:808px;top:190px}
.f-contact .row{display:flex;gap:18px;align-items:center;margin-bottom:16px;font-size:12.5px;line-height:1.6}
.f-contact .pin{width:34px;height:34px;border-radius:50%;background:#fff;display:flex;align-items:center;justify-content:center;flex:none}
.copyright{left:0;bottom:0;width:1200px;height:51px;background:var(--green);display:flex;align-items:center;justify-content:center;font-size:12px;color:#fff}
</style>
</head>
<body>

<header class="site-header">
  <div class="brand abs"><span class="mark"></span>Kestrel Vale</div>
  <nav class="nav abs"><span>BUSINESS LISTING</span><span>OUR TEAM</span><span>CONTACT US</span></nav>
  <div class="call abs">
    <span class="ico"><svg width="16" height="16" viewBox="0 0 24 24" fill="none" stroke="#fff" stroke-width="2"><path d="M5 3h4l2 5-3 2a12 12 0 0 0 6 6l2-3 5 2v4a2 2 0 0 1-2 2A17 17 0 0 1 3 5a2 2 0 0 1 2-2z"/></svg></span>
    <p>Call Us<br><b>405–555–0187</b></p>
  </div>
  <h1 class="hero-title abs">Strategically Navigating<br>Business Exits</h1>
  <p class="hero-sub abs">A Guide to Thoughtful Transitions &amp; Sustainable Success</p>
  <span class="btn hero-btn abs">CONTACT US</span>
  <div class="hero-photo abs" role="img" aria-label="Two smiling business advisors holding a laptop and tablet in front of rising arrows"></div>
</header>

<section class="about">
  <div class="frame abs"></div>
  <div class="photo abs" role="img" aria-label="Advisor reviewing a laptop with a client in a bright office"></div>
  <h2 class="abs">ABOUT OUR COMPANY</h2>
  <div class="rule" style="justify-content:flex-start"><i></i><i></i><i></i></div>
  <div class="copy abs">
    <p>At Kestrel Vale Advisors, our mission is to empower entrepreneurs and business owners by facilitating seamless transactions that lead to mutual success</p>
    <p>We understand that selling or acquiring a business can be a complex &amp; emotional journey, which is why our dedicated team of experts is here to guide you every step of the way. With a commitment to integrity, transparency, and unmatched professionalism, we strive to create a positive and rewarding experience for all our clients.</p>
  </div>
  <span class="btn olive abs">CONTACT US</span>
</section>

<section class="experience">
  <div class="head abs"><h2 class="sec-title">OUR EXPERIENCE</h2><div class="rule"><i></i><i></i><i></i></div></div>
  <div class="card abs" style="left:184px;top:146px;width:403px;height:113px"><span class="ico" role="img" aria-label="Growth icon"></span><p>With decades of experience Kestrel Vale Advisors has proudly assisted numerous clients in successfully navigating the intricate journey of selling their businesses.</p></div>
  <div class="card abs" style="left:620px;top:146px;width:403px;height:113px"><span class="ico" role="img" aria-label="Knowledge icon"></span><p>Our team brings a wealth of knowledge and expertise acquired through years of working closely with entrepreneurs and business owners across diverse industries.</p></div>
  <div class="card abs" style="left:184px;top:275px;width:403px;height:113px"><span class="ico" role="img" aria-label="Process icon"></span><p>We understand the unique challenges and complexities involved in selling a business, from valuation and marketing to negotiations and closing the deal.</p></div>
  <div class="card abs" style="left:620px;top:275px;width:403px;height:113px"><span class="ico" role="img" aria-label="Problem solving icon"></span><p>Our extensive experience allows us to anticipate potential obstacles and proactively find solutions, ensuring a seamless and efficient process for our clients.</p></div>
  <div class="card abs" style="left:184px;top:401px;width:403px;height:113px"><span class="ico" role="img" aria-label="Results icon"></span><p>We take pride in our track record of delivering exceptional results and helping our clients achieve their desired outcomes.</p></div>
  <div class="brand abs exp-logo"><span class="mark"></span>Kestrel Vale</div>
  <span class="btn abs">CONTACT US</span>
</section>

<section class="team">
  <div class="head abs"><h2 class="sec-title">OUR TEAM</h2><div class="rule"><i></i><i></i><i></i></div></div>
  <p class="intro abs">Together, our team of CPAs, attorneys, real estate brokers, and financial advisors work collaboratively to provide you with a holistic approach to business transactions. With our combined knowledge and experience, we strive to ensure a smooth and successful journey for our clients, delivering exceptional results and peace of mind.</p>
  <div class="member abs" style="left:124px"><div class="avatar" role="img" aria-label="Portrait of Nathan Ellery"></div><h3>Nathan Ellery, CPA, JD</h3><p>Finance And Legal Expertise</p></div>
  <div class="member abs" style="left:360px"><div class="avatar" role="img" aria-label="Portrait of Colby Marsh"></div><h3>Colby Marsh</h3><p>Vice President</p></div>
  <div class="member abs" style="left:597px"><div class="avatar" role="img" aria-label="Portrait of Reid Oakley"></div><h3>Reid Oakley</h3><p>Powersports &amp; Automotive Industries</p></div>
  <div class="member abs" style="left:827px"><div class="avatar" role="img" aria-label="Portrait of Walter Prescott"></div><h3>Walter Prescott</h3><p>Licensed Broker &amp; Executive</p></div>
  <div class="bio abs">
    <h3>Colby Marsh</h3>
    <p>Colby has more than 30 years of experience within the financial and insurance services fields.&nbsp; A Vice President with Harlow Stanton Reid for 13 years and a financial consultant with Meridian Mutual for 16 years.&nbsp; Much more than a "financial advisor", Colby has a keen sense to identify issues – from the basic to even the most sophisticated and complex – and quickly develop creative solutions at both personal and business levels.&nbsp; Colby finds building relationships is a key to enabling Kestrel Vale clients to make appropriate and informed decisions.</p>
  </div>
</section>

<section class="listing">
  <div class="head abs"><h2 class="sec-title">BUSINESS LISTING</h2><div class="rule"><i></i><i></i><i></i></div></div>
  <div class="tabs abs"><span class="on">Current Business Listings</span><span class="off">Recently Completed Business Sales</span></div>
  <div class="deal abs">
    <h3>Powersports Dealership</h3>
    <p class="amt">North Texas &amp; Deal Amount $1,100,000</p>
    <p>Well established multi-line dealership with strong net profit. Excellent staff in place. Dealership has a loyal customer base with further growth potential due to rapid community growth. Serious Inquires with proof of funds only.</p>
    <span class="btn">CONTACT US</span>
  </div>
  <div class="frame abs"></div>
  <div class="photo abs" role="img" aria-label="Two businessmen reviewing a tablet together"></div>
</section>

<section class="reviews">
  <div class="head abs"><h2 class="sec-title">HAPPY CUSTOMER WORDS</h2><div class="rule"><i></i><i></i><i></i></div></div>
  <span class="arrow abs" style="left:112px"><svg width="10" height="10" viewBox="0 0 10 10"><path d="M6.5 1.5 3 5l3.5 3.5" fill="none" stroke="#333" stroke-width="1.6"/></svg></span>
  <div class="quote abs" style="left:162px">
    <div class="who"><span class="face" role="img" aria-label="Customer portrait"></span>Daniel Ortiz</div>
    <svg class="mark" width="48" height="34" viewBox="0 0 48 34" fill="#ececec"><path d="M0 34V18C0 8 6 2 16 0v7c-5 2-7 5-7 10h7v17zM26 34V18c0-10 6-16 16-18v7c-5 2-7 5-7 10h7v17z"/></svg>
    <h4>Customer service was very good!</h4>
    <p>Lorem ipsum dolor sit amet, consectetuer adipiscing elit, sed diam nonummy nibh euismod tincidunt ut laoreet dolore magna aliquam erat volutpat. Ut wisi enim ad minim veniam, quis nostrud exerci tation ullamcorper suscipit lobortis.</p>
  </div>
  <div class="quote abs" style="left:612px">
    <div class="who"><span class="face" role="img" aria-label="Customer portrait"></span>Samuel K.</div>
    <svg class="mark" width="48" height="34" viewBox="0 0 48 34" fill="#ececec"><path d="M0 34V18C0 8 6 2 16 0v7c-5 2-7 5-7 10h7v17zM26 34V18c0-10 6-16 16-18v7c-5 2-7 5-7 10h7v17z"/></svg>
    <h4>Great Service And timely&nbsp; Work</h4>
    <p>Lorem ipsum dolor sit amet, consectetuer adipiscing elit, sed diam nonummy nibh euismod tincidunt ut laoreet dolore magna aliquam erat volutpat. Ut wisi enim ad minim veniam, quis nostrud exerci tation ullamcorper suscipit lobortis.</p>
  </div>
  <span class="arrow abs" style="left:1059px"><svg width="10" height="10" viewBox="0 0 10 10"><path d="M3.5 1.5 7 5 3.5 8.5" fill="none" stroke="#333" stroke-width="1.6"/></svg></span>
</section>

<section class="inquiry">
  <div class="head abs"><h2 class="sec-title">QUICK INQUIRY</h2><div class="rule"><i></i><i></i><i></i></div></div>
  <div class="field abs" style="left:264px;top:166px;width:326px"><svg width="12" height="12" viewBox="0 0 12 12" fill="none" stroke="var(--red)"><circle cx="6" cy="4" r="2.5"/><path d="M1.5 11.5c0-3 2-4.5 4.5-4.5s4.5 1.5 4.5 4.5"/></svg>Your Name*</div>
  <div class="field abs" style="left:604px;top:166px;width:327px"><svg width="12" height="12" viewBox="0 0 12 12" fill="none" stroke="var(--red)"><rect x="1" y="2.5" width="10" height="7"/><path d="m1 2.5 5 4 5-4"/></svg>Your Email*</div>
  <div class="field abs" style="left:264px;top:221px;width:326px"><svg width="12" height="12" viewBox="0 0 24 24" fill="none" stroke="var(--red)" stroke-width="2"><path d="M5 3h4l2 5-3 2a12 12 0 0 0 6 6l2-3 5 2v4a2 2 0 0 1-2 2A17 17 0 0 1 3 5a2 2 0 0 1 2-2z"/></svg>Your Phone*</div>
  <div class="field abs" style="left:604px;top:221px;width:327px;justify-content:space-between"><span style="display:flex;gap:8px;align-items:center"><svg width="12" height="12" viewBox="0 0 12 12" fill="none" stroke="var(--red)"><path d="M2 10 9 3l1 1-7 7H2z"/></svg>Inquiry For*</span><svg width="10" height="6" viewBox="0 0 10 6"><path d="m1 1 4 4 4-4" fill="none" stroke="#555"/></svg></div>
  <div class="field msg abs" style="left:264px;top:275px;width:667px"><svg width="12" height="12" viewBox="0 0 12 12" fill="none" stroke="var(--red)"><rect x="1" y="1.5" width="10" height="7"/><path d="M3 8.5v2.5l2.5-2.5"/></svg>Message*</div>
  <span class="btn abs">SUBMIT NOW</span>
</section>

<footer class="site-footer">
  <div class="brand abs"><span class="mark"></span>Kestrel Vale</div>
  <div class="f-col f-links abs"><h4>QUICK LINKS</h4><a>Home</a><a>Business Listing</a><a>Our Team</a><a>Contact Us</a></div>
  <div class="f-col f-news abs">
    <h4>NEWSLETTER SIGN UP</h4>
    <p>Sign up to hear from us about exciting new opportunities.</p>
    <div class="form"><span class="in">Enter email address</span><span class="go">SIGN UP</span></div>
  </div>
  <div class="f-contact abs">
    <div class="row"><span class="pin"><svg width="16" height="16" viewBox="0 0 24 24" fill="none" stroke="var(--red)" stroke-width="2"><path d="M12 22s7-7 7-12a7 7 0 0 0-14 0c0 5 7 12 7 12z"/><circle cx="12" cy="10" r="2.5"/></svg></span><span>482 Linden Crest Road, Harwick,<br>Oklahoma 74019, United States</span></div>
    <div class="row"><span class="pin"><svg width="16" height="16" viewBox="0 0 24 24" fill="none" stroke="var(--red)" stroke-width="2"><path d="M5 3h4l2 5-3 2a12 12 0 0 0 6 6l2-3 5 2v4a2 2 0 0 1-2 2A17 17 0 0 1 3 5a2 2 0 0 1 2-2z"/></svg></span><span>Call Us<br><b style="font-weight:600;font-size:14px">405–555–0187</b></span></div>
  </div>
  <div class="copyright abs">© 2025 Kestrel Vale Advisors. All Rights Reserved.</div>
</footer>

</body>
</html>
```